Occupational Therapy Clinic Advertisement

Create an advertisement for a magazine. Below I have attached my original ad (Ad 2020.pdf) . I want the ad changed and it should be eye catching. I would like a eye catching graphics added in the ad. It should be a graphic image that applies to education. I am attaching a sample graphic image of that I liked from someone elses ad- it should not be the same- it just is there to show what I like. Please use the same words from my original ad.Dimensions: 3.75in x 10.3 in

Target Market(s)

Parents of School aged children

Requirements
Must have
• Must have eye catching Graphic. Colors should be eye catching for a typed magazine.

```html
<!DOCTYPE html>
<html lang="en">
<head>
<meta charset="utf-8">
<title>Bright Path OT Services</title>
<link rel="stylesheet" href="https://fonts.googleapis.com/css2?family=Bebas+Neue&family=Poppins:wght@400;500;600;700&display=swap">
<style>
  :root {
    --navy: #2e3649;
    --red: #b13535;
    --teal: #2f7f6e;
    --gold: #d6a54f;
    --gray: #e1e1e1;
    --white: #ffffff;
    --ink: #1f1f1f;
    --cross: #e08a2c;
  }
  * { margin: 0; padding: 0; box-sizing: border-box; }
  html, body { width: 1200px; height: 3295px; overflow: hidden; background: var(--white); }
  .ad { position: relative; width: 1200px; height: 3295px; font-family: "Poppins", sans-serif; color: var(--ink); }
  .abs { position: absolute; }

  .header-bg, .footer-bg { position: absolute; left: 0; width: 1200px; }
  .header-bg { top: 0; height: 760px; }
  .footer-bg { top: 2520px; height: 775px; }

  .brand { left: 0; width: 1200px; top: 200px; text-align: center; font-family: "Bebas Neue", sans-serif;
    font-size: 168px; line-height: 1; color: var(--white); letter-spacing: 3px; }
  .tagline { left: 0; width: 1200px; top: 388px; text-align: center; color: var(--white);
    font-size: 44px; letter-spacing: 4px; font-weight: 400; }
  .pencil { top: 386px; height: 60px; background: linear-gradient(180deg, #c44a4a 0%, #a83131 50%, #8f2626 100%); }
  .pencil.left { left: 0; width: 235px; border-radius: 0 30px 30px 0; }
  .pencil.right { left: 975px; width: 225px; border-radius: 30px 0 0 30px; }

  .question { left: 110px; width: 994px; height: 176px; border-radius: 88px; display: flex; align-items: center; color: var(--white); }
  .question.red { top: 846px; background: var(--red); }
  .question.navy { top: 1046px; background: var(--navy); }
  .question.gold { top: 1249px; background: var(--gold); }
  .question .mark { width: 148px; height: 148px; margin-left: 14px; border-radius: 50%; background: var(--white);
    display: flex; align-items: center; justify-content: center; font-weight: 700; font-size: 110px; line-height: 1; flex-shrink: 0; }
  .question.red .mark { color: var(--red); }
  .question.navy .mark { color: var(--navy); }
  .question.gold .mark { color: var(--gold); }
  .question .words { margin-left: 44px; font-size: 42px; line-height: 1.25; }
  .question .words strong { font-weight: 700; display: block; }

  .steps { left: 110px; top: 1455px; width: 994px; height: 975px; border-radius: 44px; overflow: hidden; background: var(--white); }
  .steps-title { height: 262px; background: var(--navy); color: var(--white); font-family: "Bebas Neue", sans-serif;
    font-size: 92px; line-height: 1.02; text-align: center; padding-top: 38px; letter-spacing: 1px; }
  .struck { position: relative; display: inline-block; }
  .struck svg { position: absolute; left: -4px; top: 6px; width: calc(100% + 8px); height: 80%; }

  .step { position: absolute; left: 0; width: 994px; background: var(--gray); }
  .step.one { top: 269px; height: 234px; }
  .step.two { top: 514px; height: 219px; }
  .step.three { top: 742px; height: 233px; }
  .step .num { position: absolute; left: 0; top: 0; width: 233px; height: 100%; color: var(--white);
    font-family: "Bebas Neue", sans-serif; font-size: 220px; display: flex; align-items: center; justify-content: center; padding-top: 14px; }
  .step .num::after { content: ""; position: absolute; right: -34px; top: 50%; transform: translateY(-50%);
    border-top: 34px solid transparent; border-bottom: 34px solid transparent; border-left: 34px solid; }
  .step.one .num { background: var(--red); } .step.one .num::after { border-left-color: var(--red); }
  .step.two .num { background: var(--teal); } .step.two .num::after { border-left-color: var(--teal); }
  .step.three .num { background: var(--gold); } .step.three .num::after { border-left-color: var(--gold); }
  .step .text { position: absolute; left: 322px; top: 44px; font-size: 40px; line-height: 1.22; }
  .step .text h3 { font-size: 48px; font-weight: 600; line-height: 1.2; }
  .step.one h3 { color: var(--red); } .step.two h3 { color: var(--teal); } .step.three h3 { color: var(--gold); }
  .step .note { position: absolute; right: 46px; bottom: 32px; font-size: 27px; font-style: italic; text-align: right; line-height: 1.3; }

  .footer { left: 102px; top: 2718px; color: var(--white); }
  .footer .accepted { font-size: 52px; font-weight: 700; color: var(--gold); line-height: 1.2; margin-bottom: 24px; }
  .footer p { font-size: 35px; line-height: 1.4; }
  .footer .gap { margin-top: 14px; }
  .footer .dots { color: var(--gold); font-size: 50px; letter-spacing: 2px; line-height: 0.8; margin: 22px 0 26px; font-weight: 700; }
  .footer .name { font-size: 53px; font-weight: 700; line-height: 1.2; }
  .footer .phone { font-size: 35px; margin-top: 12px; }
</style>
</head>
<body>
<div class="ad">
  <svg class="header-bg" viewBox="0 0 1200 760" aria-hidden="true">
    <rect x="0" y="0" width="1200" height="590" fill="#2e3649"/>
    <circle cx="60" cy="560" r="130" fill="#2e3649"/>
    <circle cx="250" cy="620" r="120" fill="#2e3649"/>
    <circle cx="470" cy="600" r="140" fill="#2e3649"/>
    <circle cx="700" cy="640" r="110" fill="#2e3649"/>
    <circle cx="900" cy="610" r="135" fill="#2e3649"/>
    <circle cx="1110" cy="570" r="140" fill="#2e3649"/>
  </svg>

  <div class="abs brand">BRIGHT PATH</div>
  <div class="abs pencil left" role="img" aria-label="Red pencil graphic"></div>
  <div class="abs tagline">OT SERVICES&nbsp;&nbsp;718 555-0142</div>
  <div class="abs pencil right" role="img" aria-label="Red pencil graphic"></div>

  <div class="abs question red">
    <div class="mark">?</div>
    <div class="words"><strong>Does Your Child</strong>Struggle With Reading/kriah?</div>
  </div>
  <div class="abs question navy">
    <div class="mark">?</div>
    <div class="words"><strong>Knows The Information</strong>But Fails The Test?</div>
  </div>
  <div class="abs question gold">
    <div class="mark">?</div>
    <div class="words"><strong>Has Difficulty Remembering</strong>Names And Dates?</div>
  </div>

  <div class="abs steps">
    <div class="steps-title">YES, YOUR CHILD <span class="struck">CAN<svg viewBox="0 0 100 100" preserveAspectRatio="none" aria-hidden="true"><path d="M8 8 L92 92 M92 8 L8 92" stroke="#e08a2c" stroke-width="12" fill="none"/></svg></span> WILL<br>SUCCEED IN SCHOOL?</div>

    <div class="step one">
      <div class="num">1</div>
      <div class="text"><h3>We Evaluate:</h3>Using Strandardized<br>Evaluations</div>
    </div>
    <div class="step two">
      <div class="num">2</div>
      <div class="text"><h3>We Treat:</h3>Using Researched<br>Based Techinques</div>
    </div>
    <div class="step three">
      <div class="num">3</div>
      <div class="text"><h3>Ages:</h3>6-18</div>
      <div class="note">* We Treat The<br>Underlying Processing Deficits</div>
    </div>
  </div>

  <svg class="footer-bg" viewBox="0 0 1200 775" aria-hidden="true">
    <rect x="0" y="150" width="1200" height="625" fill="#2e3649"/>
    <circle cx="50" cy="170" r="110" fill="#2e3649"/>
    <circle cx="270" cy="130" r="125" fill="#2e3649"/>
    <circle cx="500" cy="160" r="105" fill="#2e3649"/>
    <circle cx="770" cy="110" r="120" fill="#2e3649"/>
    <circle cx="960" cy="80" r="110" fill="#2e3649"/>
    <circle cx="1150" cy="120" r="115" fill="#2e3649"/>
  </svg>

  <div class="abs footer">
    <div class="accepted">Board Of Ed OT RSA’s&nbsp; Accepted</div>
    <p>Located in Borough Park</p>
    <p>Evaluations done in Borough PArk &amp; Staten Island</p>
    <p class="gap">For More Information Or To Be Added To Our Email List,</p>
    <p><strong>Please Email: brightpathot@example.com</strong></p>
    <div class="dots">•••</div>
    <div class="name">Dana Weller OTR/L</div>
    <div class="phone">(718) 555 - 0142</div>
  </div>
</div>
</body>
</html>
```